Banner Ads for Online Poker Promotion

We are an online poker network, the KLV (www.theklvnet.eu). We are looking for a small selection of web banner ads for our latest promotion.

Banner sizes that we need are:
- 196x523 (static .psd and .png)
- 199x129 (static .psd and .png)
- 447x426 (static .psd and .png)
- 500x400 (static .psd and .png)
- 697x167 (static .psd and .png)
- 460x60 (animated .gif)

The promotion name is ‘Rush & Deal Plunder’ (or ‘RND Plunder’) and the concept is that certain Sit & Go tournaments have money added to the prize pool. Basically, free cash for Sit & Go players.

(If you don’t know poker, a ‘Sit & Go’ is a tournament which starts when a specific number of players join, as opposed to a scheduled tournament which starts at a specific time).

The promotion starts on November 3rd.

Guidelines:

The name of the promotion, ‘Rush & Deal Plunder’ or ‘RND Plunder’, should feature prominently in the banners.

The strap line can be ‘Get Your Share of the Loot’, ‘Added Money in SNGs’ or something similar (feel free to be creative).

Our network logo (attached) must feature on the animated .gif. It is optional on the other banners.

Examples of past promotional imagery can be found on our website, in particular these pages: http://www.theklvnet.eu/promotions/ and http://www.theklvnet.eu/promotions/archived-promotions/ . Our last promotion was crowdsourced and the details of that and the winner can be found here: http://jobs.artquarry.com/job.aspx?id=512047

We are looking to go in a more modern and risqué direction than the past, in order to stand out from competition which is very bland.

Common poker imagery –cards, chips, suit icons etc – or objects associated with live poker (tables, etc) is a little clichéd. It can be included if it has a clear purpose. But don’t just put flying cards or suit symbols in there for no reason.

More like vexOS4/5, less like vexOS3

Think flat, modern, glamour, clean, fresh, bright, rock music, extreme sports, and the Loud Stone!

Most of our customers are 18-35, male, and we have a strong European focus.

As we are a gaming company, the banners must not encourage underage play, problem gambling, or associate gambling with sexual or social success.

If any further guidance is needed please don’t hesitate to ask!

```html
<!DOCTYPE html>
<html lang="en">
<head>
<meta charset="utf-8">
<title>Rush &amp; Deal Plunder — KLV</title>
<link rel="stylesheet" href="https://fonts.googleapis.com/css2?family=Anton&family=Bebas+Neue&family=Oswald:wght@500&display=swap">
<style>
  :root {
    --ink-deep: #05080f;
    --ink-mid: #0b1626;
    --ray-bright: #2f7fd6;
    --ray-mid: #1b5aa8;
    --ray-dark: #123f7c;
    --gold-light: #fff3c4;
    --gold: #e8b947;
    --gold-dark: #9a6a16;
    --white: #f4f6fa;
  }
  * { margin: 0; padding: 0; box-sizing: border-box; }
  html, body {
    width: 1200px; height: 960px; overflow: hidden;
    background: var(--ink-deep);
  }
  .banner {
    position: relative;
    width: 1200px; height: 960px;
    overflow: hidden;
    background: radial-gradient(ellipse at 50% 45%, var(--ink-mid) 0%, var(--ink-deep) 75%);
  }
  .rays { position: absolute; inset: 0; width: 1200px; height: 960px; }
  .rule {
    position: absolute; left: 408px; width: 384px; height: 4px;
    background: var(--white);
  }
  .rule--top { top: 106px; }
  .rule--bottom { top: 712px; }
  .title {
    position: absolute; left: 0; width: 1200px;
    text-align: center;
    font-family: "Anton", "Impact", sans-serif;
    text-transform: uppercase;
    line-height: 1;
    background: linear-gradient(180deg, var(--gold-light) 0%, var(--gold) 45%, var(--gold-dark) 60%, var(--gold) 80%, var(--gold-light) 100%);
    -webkit-background-clip: text; background-clip: text;
    color: transparent;
    -webkit-text-stroke: 2px #5a3a08;
    filter: drop-shadow(0 6px 8px rgba(0,0,0,0.6));
  }
  .title__lead { top: 150px; font-size: 150px; letter-spacing: 6px; }
  .title__main { top: 320px; font-size: 236px; letter-spacing: 4px; }
  .strapline {
    position: absolute; top: 596px; left: 0; width: 1200px;
    text-align: center;
    font-family: "Bebas Neue", "Oswald", sans-serif;
    font-size: 62px; letter-spacing: 4px;
    color: var(--white);
    text-shadow: 0 3px 6px rgba(0,0,0,0.7);
  }
  .network-name {
    position: absolute; top: 838px; left: 0; width: 1200px;
    text-align: center;
    font-family: "Oswald", sans-serif;
    font-weight: 500; font-size: 54px; letter-spacing: 3px;
    color: var(--white);
  }
</style>
</head>
<body>
<main class="banner">
  <svg class="rays" viewBox="0 0 1200 960" aria-hidden="true">
    <g opacity="0.85">
      <polygon points="600,450 0,60 0,300" fill="var(--ray-mid)"/>
      <polygon points="600,450 180,0 520,0" fill="var(--ray-dark)"/>
      <polygon points="600,450 760,0 1080,0" fill="var(--ray-mid)"/>
      <polygon points="600,450 1200,120 1200,420" fill="var(--ray-bright)"/>
      <polygon points="600,450 1200,620 1200,900" fill="var(--ray-dark)"/>
      <polygon points="600,450 980,960 700,960" fill="var(--ray-mid)"/>
      <polygon points="600,450 420,960 120,960" fill="var(--ray-bright)"/>
      <polygon points="600,450 0,560 0,820" fill="var(--ray-dark)"/>
    </g>
    <g opacity="0.5">
      <polygon points="600,450 300,0 420,0" fill="var(--ray-bright)"/>
      <polygon points="600,450 1200,300 1200,360" fill="var(--white)" opacity="0.3"/>
      <polygon points="600,450 0,400 0,480" fill="var(--ray-bright)"/>
    </g>
  </svg>

  <div class="rule rule--top"></div>
  <h1>
    <span class="title title__lead">Rush &amp; Deal</span>
    <span class="title title__main">Plunder</span>
  </h1>
  <p class="strapline">Get your share of the loot</p>
  <div class="rule rule--bottom"></div>
  <div class="network-name">KLV</div>
</main>
</body>
</html>
```